Korvix App Graphics Design

Our application promotes location based self expression via pictures and text. The primary focus of the application is on the content posted and not on the person that posted it.

We want a very clean and fresh design that evokes positive energy. Our site is unique so our design should be as well. People will reveal thoughts on our site, so the design should convey a "revealing" feel. Our site is a place where people are comfortable to freely express themselves. Colors we have in mind are blue and green hues with earth tones for background.

Our project is to design ten screens for our Korvix application at resolution of 1136-by-640 pixels:

Feed Screen
Camera Screen
Post Screen
Check In Screen
Approval Screen
Map Screen
Flag Screen
Feed Select Screen
Export Screen
Menu Screen

In the contest phase we will require only three screens to be submitted. The screens we require to be submitted are: Feed Screen; Map Screen and Camera Screen. The designer we select as the winner of the competition will then complete the project and deliver a total of the ten screens described above in the handover phase.

We have attached a document below with detailed specs of each screen, we ask for your innovation to bring these screens to life through your design.
Updates

We want to clarify one aspect regarding the VISOR: the visor needs to be transparent so that when the picture scrolls underneath it, you can still see the picture underneath the visor.

Hi Everyone,

We have noticed that some designers need clarification regarding the visor element in the feed screen.
I have attached two examples to our brief area called:
Visor Example 1 and Visor Example 2

Please note that these are not the style we are looking for but are a good example to the concept of a Transparent Visor above the feed stream. We are looking for you guys to come up with a Visor concept that is consistent with the style of the design you are submitting.

Thanks,

Bo

Target Market(s)

People 17-40 who want to share their thought about the world around them.

Industry/Entity Type

Flag

Font styles to use
Sans Serif
Other font styles liked:
• We like “Helvetica New” or “Avenir” but are flexible

Requirements
Must have
• Visor component should look innovative.

```html
<!DOCTYPE html>
<html lang="en">
<head>
<meta charset="utf-8">
<title>Korvix Feed</title>
<link rel="stylesheet" href="https://fonts.googleapis.com/css2?family=Roboto:wght@300;400&display=swap">
<style>
:root{
  --visor:rgba(84,132,192,.88);
  --tile:rgba(230,230,232,.92);
  --stat:rgba(120,150,200,.7);
  --action:rgba(52,120,192,.9);
  --action-light:rgba(150,180,225,.75);
  --place:rgba(232,158,38,.9);
  --next:rgba(204,62,112,.88);
  --dock:#0e72bf;
  --dock-btn:#5f93d3;
  --ink:#2b2b2b;
  --white:#ffffff;
}
*{margin:0;padding:0;box-sizing:border-box}
html,body{width:676px;height:1200px;overflow:hidden;background:#fff}
body{font-family:"Roboto",sans-serif;position:relative}
.feed-photo{position:absolute;left:0;top:0;width:676px;height:1120px;
  background:linear-gradient(180deg,#87817f 0%,#a9a29c 14%,#d8c9ae 28%,#f1cf7a 40%,#f6b33a 46%,#c98a3a 50%,#e4b66a 54%,#f2d7a0 62%,#e9c890 72%,#b79a55 82%,#a88a3c 100%)}
.tile{position:absolute;width:80px;height:54px;background:var(--tile);box-shadow:0 2px 4px rgba(0,0,0,.35);display:flex;align-items:center;justify-content:center}
.tile svg{width:44px;height:30px}
.tile-menu{left:38px;top:42px}
.tile-key{left:564px;top:42px}
.tile-block{left:38px;top:193px;height:52px}
.tile-share{left:564px;top:193px;height:52px}
.visor{position:absolute;left:0;top:97px;width:676px;height:96px;background:var(--visor);box-shadow:0 3px 6px rgba(0,0,0,.25);color:var(--white);font-weight:400;font-size:32px;padding-left:33px;display:flex;align-items:center}
.stats{position:absolute;top:809px;left:34px;height:55px;display:flex;gap:2px}
.stat{background:var(--stat);color:var(--white);font-size:32px;font-weight:400;display:flex;align-items:center;justify-content:center;height:55px}
.stat-distance{width:153px}
.stat-id{width:295px}
.stat-time{width:154px}
.rating{position:absolute;top:877px;left:0;width:676px;height:79px;background:var(--action);color:var(--white);font-size:31px}
.rating .arrow{position:absolute;top:0;height:79px;width:84px;background:var(--action-light);display:flex;align-items:center;justify-content:center}
.arrow-up{left:34px}
.arrow-down{left:566px;width:76px!important}
.rating .label{position:absolute;top:0;height:79px;display:flex;align-items:center}
.label-promote{left:150px}
.label-demote{left:388px}
.rating .divider{position:absolute;left:337px;top:0;width:2px;height:79px;background:var(--white)}
.place{position:absolute;top:958px;left:0;width:676px;height:79px;background:var(--place);color:var(--ink);font-size:21px;line-height:28px;padding:12px 0 0 34px}
.next{position:absolute;top:1039px;left:0;width:676px;height:81px;background:var(--next);color:var(--white);font-size:46px;font-weight:400;display:flex;align-items:center;justify-content:center}
.dock{position:absolute;top:1120px;left:0;width:676px;height:80px;background:var(--dock)}
.dock-btn{position:absolute;top:0;width:82px;height:51px;background:var(--dock-btn);display:flex;align-items:center;justify-content:center}
.dock-camera{left:32px}
.dock-burst{left:564px}
</style>
</head>
<body>
<div class="feed-photo" role="img" aria-label="Sunrise over a misty pond with a white wooden boathouse and its reflection"></div>

<div class="tile tile-menu"><svg viewBox="0 0 44 30"><g fill="#fff"><circle cx="4" cy="5" r="3"/><circle cx="4" cy="15" r="3"/><circle cx="4" cy="25" r="3"/><rect x="10" y="3" width="32" height="4"/><rect x="10" y="13" width="32" height="4"/><rect x="10" y="23" width="32" height="4"/></g></svg></div>
<div class="tile tile-key"><svg viewBox="0 0 44 30"><g fill="none" stroke="#fff" stroke-width="3"><circle cx="12" cy="15" r="9"/><path d="M21 15h18"/></g><circle cx="37" cy="15" r="4" fill="#fff"/></svg></div>

<div class="visor">Golden Morning</div>

<div class="tile tile-block"><svg viewBox="0 0 44 30"><g fill="none" stroke="#fff" stroke-width="3"><circle cx="22" cy="15" r="10"/><path d="M15 8l14 14"/></g></svg></div>
<div class="tile tile-share"><svg viewBox="0 0 44 30"><g fill="#fff"><path d="M22 2l8 10h-5v10h-6V12h-5z"/><rect x="6" y="23" width="32" height="3"/></g></svg></div>

<div class="stats">
  <div class="stat stat-distance">105.10 M</div>
  <div class="stat stat-id">1014566</div>
  <div class="stat stat-time">10:12:20</div>
</div>

<div class="rating">
  <div class="arrow arrow-up"><svg width="38" height="32" viewBox="0 0 38 32"><path d="M19 0l19 32H0z" fill="#fff"/></svg></div>
  <div class="label label-promote">PROMOTE</div>
  <div class="divider"></div>
  <div class="label label-demote">DEMOTE</div>
  <div class="arrow arrow-down"><svg width="38" height="32" viewBox="0 0 38 32"><path d="M0 0h38L19 32z" fill="#fff"/></svg></div>
</div>

<div class="place">Maple Grill<br>48 Harbor Lane, Westfield,&nbsp; NY10021</div>

<div class="next">Next Picture</div>

<div class="dock">
  <div class="dock-btn dock-camera"><svg width="42" height="26" viewBox="0 0 42 26"><g fill="none" stroke="#fff" stroke-width="2"><rect x="1" y="1" width="40" height="24"/><circle cx="14" cy="13" r="5"/></g><rect x="30" y="6" width="6" height="4" fill="#fff"/></svg></div>
  <div class="dock-btn dock-burst"><svg width="32" height="32" viewBox="0 0 32 32"><path d="M16 2l3 8 7-5-3 8 8 1-7 4 5 7-8-2v8l-5-7-5 7v-8l-8 2 5-7-7-4 8-1-3-8 7 5z" fill="none" stroke="#fff" stroke-width="1.6" stroke-linejoin="round"/></svg></div>
</div>
</body>
</html>
```